New Business cards design and layout
Verant cards
New Business cards design and layout - Information Technology
Creative Brief
Professional
Dorian T. Halvek
VP, Sales and Business Development
4718 - 12th Avenue N.W. Calgary, Alberta T3K 1R8
dorian@verantinfo.ca
www.verantinfo.ca

```html
<!DOCTYPE html>
<html lang="en">
<head>
<meta charset="utf-8">
<title>Verant Business Cards</title>
<link rel="stylesheet" href="https://fonts.googleapis.com/css2?family=Exo+2:wght@400;600;700&display=swap">
<style>
  :root {
    --page: #c9c9cb;
    --card: #ffffff;
    --blue: #1e50d6;
    --blue-dark: #1438a8;
    --grey: #8a8d92;
    --grey-light: #b8bbc0;
    --ink: #3a3d44;
  }
  * { box-sizing: border-box; margin: 0; padding: 0; }
  html, body { width: 1200px; height: 895px; overflow: hidden; }
  body {
    background: var(--page);
    font-family: "Exo 2", Arial, sans-serif;
    color: var(--ink);
    position: relative;
  }
  .card {
    position: absolute;
    left: 250px;
    width: 700px;
    height: 400px;
    background: var(--card);
    overflow: hidden;
    box-shadow: 0 4px 14px rgba(0,0,0,0.18);
  }
  .card--back { top: 35px; }
  .card--front { top: 460px; }
  .card__frame {
    position: absolute;
    inset: 22px;
    border: 2px solid var(--grey-light);
    z-index: 2;
    pointer-events: none;
  }
  .card__band {
    position: absolute;
    left: 0; right: 0;
    background: var(--blue);
  }
  .card--back .card__band { bottom: 70px; height: 62px; }
  .card--front .card__band { bottom: 18px; height: 44px; }
  .card__wedge {
    position: absolute;
    left: 0;
    bottom: 62px;
    width: 0; height: 0;
    border-left: 150px solid var(--grey);
    border-top: 90px solid transparent;
    opacity: .55;
  }
  .logo {
    display: flex;
    align-items: center;
    gap: 12px;
    color: var(--blue);
    font-weight: 700;
    letter-spacing: 3px;
    text-transform: uppercase;
  }
  .logo__mark {
    width: 22px; height: 22px;
    background: var(--grey);
  }
  .card--back .logo {
    position: absolute;
    top: 115px; left: 0; right: 0;
    justify-content: center;
    font-size: 56px;
  }
  .back__web {
    position: absolute;
    left: 0; right: 0;
    bottom: 86px;
    text-align: center;
    color: #fff;
    font-size: 26px;
    letter-spacing: 1px;
    z-index: 3;
  }
  .card--front .logo {
    position: absolute;
    top: 52px; left: 52px;
    font-size: 40px;
  }
  .contact {
    position: absolute;
    display: flex;
    flex-direction: column;
    gap: 16px;
    font-size: 15px;
  }
  .contact--left { left: 52px; top: 160px; }
  .contact--right { left: 360px; top: 250px; gap: 12px; }
  .contact__row { display: flex; align-items: flex-start; gap: 12px; line-height: 1.35; }
  .contact__icon {
    flex: none;
    width: 20px; height: 20px;
    background: var(--blue);
    border-radius: 3px;
    display: flex; align-items: center; justify-content: center;
  }
  .person {
    position: absolute;
    left: 360px; top: 150px;
  }
  .person__name { color: var(--blue); font-size: 26px; font-weight: 600; }
  .person__title { font-size: 14px; margin-top: 2px; }
</style>
</head>
<body>

<section class="card card--back">
  <div class="card__frame"></div>
  <div class="logo"><span class="logo__mark"></span>Verant</div>
  <div class="card__band"></div>
  <p class="back__web">www.verantinfo.ca</p>
</section>

<section class="card card--front">
  <div class="card__frame"></div>
  <div class="logo"><span class="logo__mark"></span>Verant</div>

  <div class="contact contact--left">
    <div class="contact__row">
      <span class="contact__icon">
        <svg width="12" height="12" viewBox="0 0 12 12"><path d="M3 1 L5 3.5 L4 5 Q5 7 7 8 L8.5 7 L11 9 L10 11 Q4 11 1 2 Z" fill="#fff"/></svg>
      </span>
      <span>403 555 0187</span>
    </div>
    <div class="contact__row">
      <span class="contact__icon">
        <svg width="12" height="10" viewBox="0 0 12 10"><rect x="0.5" y="0.5" width="11" height="9" fill="none" stroke="#fff"/><path d="M0.5 0.5 L6 5.5 L11.5 0.5" fill="none" stroke="#fff"/></svg>
      </span>
      <span>dorian@verantinfo.ca</span>
    </div>
  </div>

  <div class="person">
    <p class="person__name">Dorian T. Halvek</p>
    <p class="person__title">VP, Sales and Business Development</p>
  </div>

  <div class="contact contact--right">
    <div class="contact__row">
      <span class="contact__icon">
        <svg width="10" height="13" viewBox="0 0 10 13"><path d="M5 12 C1 7 1 5.5 1 4.5 A4 4 0 0 1 9 4.5 C9 5.5 9 7 5 12 Z" fill="#fff"/><circle cx="5" cy="4.5" r="1.5" fill="#1e50d6"/></svg>
      </span>
      <span>4718 - 12th Avenue N.W.<br>Calgary, Alberta T3K 1R8</span>
    </div>
    <div class="contact__row">
      <span class="contact__icon">
        <svg width="12" height="12" viewBox="0 0 12 12"><circle cx="6" cy="6" r="5" fill="none" stroke="#fff"/><ellipse cx="6" cy="6" rx="2.2" ry="5" fill="none" stroke="#fff"/><path d="M1 6 H11" stroke="#fff"/></svg>
      </span>
      <span>www.verantinfo.ca</span>
    </div>
  </div>

  <div class="card__wedge"></div>
  <div class="card__band"></div>
</section>

</body>
</html>
```